Want to incorporate elements of all these items to make an amazing sign to welcome people to the community. The sign is 6x4 and needs to incorporate the following items:

Welcome to Thistle Grove

Come visit the DWR sales center at 548 marlow road
High Speed Fiber Internet
Land financing starting at $299 (No credit checks)
Let us build your dream home!
517-384-2296
We like the gold and black design no teal or blue that was another agents design. Some combination of the current sign all the stuff listed above and then design elements that tie into the truck wrap.

Target Market(s)

People visiting the neighborhood

Industry/Entity Type

real estate and construction

Font styles to use
Serif

Colors

Designer to choose colors to be used in the design.

Requirements
Must have
• DWR Home Builders Welcomes you to Thistle Grove, Let us build your dream home, Phone number, Land financing starting at $299 NO credit checks

```html
<!DOCTYPE html>
<html lang="en">
<head>
<meta charset="utf-8">
<title>Thistle Grove Welcome Sign</title>
<link rel="stylesheet" href="https://fonts.googleapis.com/css2?family=Great+Vibes&family=Montserrat:wght@600;700;800&display=swap">
<style>
  :root {
    --page: #ffffff;
    --sign-black: #000000;
    --sheet-light: #9a9a9a;
    --sheet-mid: #5a5a5a;
    --white: #ffffff;
    --ink: #000000;
    --accent-orange: #ff3d00;
    --gold-light: #f3dc8a;
    --gold: #c9a24a;
    --gold-dark: #8a6420;
  }
  * { margin: 0; padding: 0; box-sizing: border-box; }
  html, body { width: 1200px; height: 1000px; overflow: hidden; background: var(--page); }
  .canvas { position: relative; width: 1200px; height: 1000px; }
  .sign {
    position: absolute; left: 128px; top: 186px; width: 945px; height: 628px;
    background: var(--sign-black); overflow: hidden; border: 1px solid #777;
    font-family: "Montserrat", sans-serif; color: var(--white);
  }
  .blueprint-left {
    position: absolute; left: 0; top: 0; width: 560px; height: 628px;
    background: linear-gradient(120deg, var(--sheet-light) 0%, var(--sheet-mid) 30%, rgba(0,0,0,0) 62%);
  }
  .blueprint-right {
    position: absolute; right: 0; top: 0; width: 520px; height: 628px;
    background: linear-gradient(295deg, #c8c8c8 0%, #8c8c8c 28%, rgba(0,0,0,0) 60%);
  }
  .outlined {
    -webkit-text-stroke: 6px var(--ink); paint-order: stroke fill;
    text-shadow: 3px 3px 0 var(--ink);
  }
  .welcome {
    position: absolute; left: 0; right: 0; top: 62px; text-align: center;
    font-family: "Great Vibes", cursive; font-size: 92px; line-height: 1;
  }
  .visit-line {
    position: absolute; left: 0; right: 0; top: 218px;
    display: flex; justify-content: center; align-items: center; gap: 16px;
    font-weight: 800; font-size: 37px; letter-spacing: -0.5px;
  }
  .builder-name {
    font-weight: 800; font-size: 96px; color: var(--gold); letter-spacing: -2px;
    line-height: 1;
  }
  .address {
    position: absolute; left: 0; right: 0; top: 308px; text-align: center;
    font-weight: 600; font-size: 22px; line-height: 1.45;
  }
  .perk {
    position: absolute; color: var(--accent-orange); font-weight: 700;
    text-align: center; line-height: 1.25;
    -webkit-text-stroke: 4px var(--ink); paint-order: stroke fill;
  }
  .perk-internet { left: 40px; width: 195px; top: 310px; font-size: 25px; }
  .perk-financing { left: 650px; width: 280px; top: 298px; font-size: 22px; }
  .dream {
    position: absolute; left: 0; right: 0; top: 405px; text-align: center;
    font-weight: 700; font-size: 43px;
  }
  .phone {
    position: absolute; left: 0; right: 0; top: 465px; text-align: center;
    font-weight: 700; font-size: 104px; line-height: 1.1; letter-spacing: 1px;
    background: linear-gradient(180deg, var(--gold-light) 0%, var(--gold) 50%, var(--gold-dark) 100%);
    -webkit-background-clip: text; background-clip: text; color: transparent;
    filter: drop-shadow(3px 3px 0 var(--ink));
  }
</style>
</head>
<body>
<div class="canvas">
  <section class="sign">
    <div class="blueprint-left" role="img" aria-label="Hand sketching a subdivision lot plan with a pencil"></div>
    <div class="blueprint-right" role="img" aria-label="Rolled architectural floor plans"></div>

    <h1 class="welcome outlined">Welcome to Thistle Grove</h1>

    <div class="visit-line">
      <span class="outlined">COME VISIT THE</span>
      <span class="builder-name">DWR</span>
      <span class="outlined">SALES CENTER</span>
    </div>

    <p class="address">AT<br>548 MARLOW ROAD</p>

    <p class="perk perk-internet">High Speed<br>Fiber Internet</p>
    <p class="perk perk-financing">LAND FINANCING<br>STARTING AT $299<br>(NO CREDIT CHECKS)</p>

    <p class="dream outlined">Let us build your dream home!</p>
    <p class="phone">517-384-2296</p>
  </section>
</div>
</body>
</html>
```